Update Business Card Design

I'm looking to update my business cards. Attached is a photo of the current design. I like the black side so that does not have to be update. The white side needs to be updated. I want the design to be modern and minimalistic.
I am a lawyer and my firm's website is www.brennoxlegalco.com (for reference).
My firm's logo has a horizontal version (which is on the black side of the card) and a vertical version (on the white side). I would prefer to keep the vertical version on the white side and horizontal version on the black side (the logo files are attached).

I am open to redesigning the black side also. I would like one side to have the horizontal logo and the other to have the vertical logo.

```html
<!DOCTYPE html>
<html lang="en">
<head>
<meta charset="utf-8">
<title>Brennox Legal Co. — Business Card</title>
<link rel="stylesheet" href="https://fonts.googleapis.com/css2?family=Lora:wght@400;600&display=swap">
<style>
  :root {
    --page-bg: #d9d4cc;
    --card-dark: #1c1c1e;
    --card-dark-2: #2c2c2f;
    --frost-1: #e9eaec;
    --frost-2: #cfd3d8;
    --frost-3: #e3ddd6;
    --teal: #1a8aa6;
    --teal-deep: #0f6f86;
    --text-light: #e4e4e4;
    --text-muted: #c9c9c9;
    --ink: #1a1a1a;
  }
  * { margin: 0; padding: 0; box-sizing: border-box; }
  html, body { width: 1200px; height: 970px; overflow: hidden; }
  body {
    background: var(--page-bg);
    font-family: "Lora", Georgia, serif;
    position: relative;
  }
  .card {
    position: absolute;
    left: 60px; top: 175px;
    width: 1080px; height: 620px;
    border-radius: 26px;
    overflow: hidden;
    box-shadow: 0 18px 40px rgba(0,0,0,.25);
  }
  .card-surface { position: absolute; inset: 0; }
  .card-text { position: absolute; white-space: nowrap; }
  .holder-name {
    left: 59px; top: 72px;
    font-size: 34px; font-weight: 600; letter-spacing: 1px;
    color: var(--text-light);
  }
  .holder-title {
    left: 59px; top: 118px;
    font-size: 25px; color: var(--teal);
  }
  .name-marker {
    position: absolute; left: -33px; top: 90px;
    width: 66px; height: 66px; border-radius: 50%;
    background: var(--teal);
  }
  .office-address {
    left: 59px; top: 250px;
    font-size: 25px; line-height: 32px; color: var(--text-muted);
  }
  .contact-list {
    position: absolute; left: 59px; top: 392px;
    list-style: none;
  }
  .contact-item {
    display: flex; align-items: center; gap: 18px;
    height: 34.5px;
    font-size: 25px; color: var(--text-muted);
  }
  .contact-item.email { font-size: 22px; }
  .contact-icon { width: 29px; height: 29px; flex: none; }
  .firm-mark {
    position: absolute; left: 770px; top: 140px;
    width: 96px; height: 96px; border-radius: 50%;
    background: var(--teal-deep);
  }
  .firm-rule {
    position: absolute; left: 682px; top: 358px;
    width: 272px; height: 4px; background: var(--ink);
    border-radius: 2px;
  }
  .firm-name {
    position: absolute; left: 640px; width: 356px; top: 378px;
    text-align: center;
    font-size: 54px; line-height: 64px; font-weight: 400;
    color: var(--ink); letter-spacing: 1px;
  }
</style>
</head>
<body>
  <div class="card">
    <svg class="card-surface" width="1080" height="620" viewBox="0 0 1080 620">
      <defs>
        <linearGradient id="frost" x1="0" y1="0" x2="1" y2="1">
          <stop offset="0" stop-color="#e5e1da"/>
          <stop offset=".45" stop-color="#eef1f4"/>
          <stop offset="1" stop-color="#d8d2ca"/>
        </linearGradient>
        <radialGradient id="dark" cx=".35" cy=".5" r=".7">
          <stop offset="0" stop-color="#2c2c2f"/>
          <stop offset="1" stop-color="#18181a"/>
        </radialGradient>
      </defs>
      <rect class="frosted-side" width="1080" height="620" fill="url(#frost)"/>
      <path class="dark-side" d="M0 0 H558 Q470 310 563 620 H0 Z" fill="url(#dark)"/>
      <path class="accent-curve" d="M566 0 Q478 310 571 620" fill="none" stroke="#1a8aa6" stroke-width="5"/>
      <path class="accent-curve-thin" d="M578 30 Q500 310 580 600" fill="none" stroke="#0f6f86" stroke-width="2" opacity=".6"/>
    </svg>

    <span class="name-marker"></span>
    <p class="card-text holder-name">ADRIAN MARLOW</p>
    <p class="card-text holder-title">Attorney at Law</p>

    <p class="card-text office-address">318 Larkfield Avenue<br>Suite 410<br>Westbrook, CA 90512</p>

    <ul class="contact-list">
      <li class="contact-item">
        <svg class="contact-icon" viewBox="0 0 30 30"><rect width="30" height="30" rx="4" fill="#1a8aa6"/><rect x="10" y="6" width="10" height="18" rx="1.5" fill="none" stroke="#1c1c1e" stroke-width="2.5"/></svg>
        310.555.0142
      </li>
      <li class="contact-item">
        <svg class="contact-icon" viewBox="0 0 30 30"><rect width="30" height="30" rx="4" fill="#1a8aa6"/><path d="M6 12 Q15 5 24 12 L22 15 L18 13 L12 13 L8 15 Z" fill="#1c1c1e"/><rect x="9" y="15" width="12" height="8" rx="1" fill="#1c1c1e"/></svg>
        310.555.0187
      </li>
      <li class="contact-item">
        <svg class="contact-icon" viewBox="0 0 30 30"><rect width="30" height="30" rx="4" fill="#1a8aa6"/><rect x="10" y="6" width="10" height="6" fill="#1c1c1e"/><rect x="6" y="12" width="18" height="8" rx="1" fill="#1c1c1e"/><rect x="10" y="18" width="10" height="6" fill="#1c1c1e"/></svg>
        310.555.0163
      </li>
      <li class="contact-item email">
        <svg class="contact-icon" viewBox="0 0 30 30"><rect width="30" height="30" rx="4" fill="#1a8aa6"/><rect x="6" y="9" width="18" height="12" fill="none" stroke="#1c1c1e" stroke-width="2"/><path d="M6 9 L15 16 L24 9" fill="none" stroke="#1c1c1e" stroke-width="2"/></svg>
        adrian@BrennoxLegalCo.com
      </li>
    </ul>

    <span class="firm-mark"></span>
    <span class="firm-rule"></span>
    <p class="firm-name">BRENNOX<br>LEGAL CO.</p>
  </div>
</body>
</html>
```